Door Knocker Design Front & Back

Front needs to be attention grabbing. Would like to highlight that we offer financing as well. Size of this needs to be 4" x 11".
Attached is our business cards front and back as well as our logo+

```html
<!DOCTYPE html>
<html lang="en">
<head>
<meta charset="utf-8">
<title>HVR Remodeling &amp; Restoration – Door Hanger Front &amp; Back</title>
<link href="https://fonts.googleapis.com/css2?family=Oswald:wght@500;600;700&family=Orbitron:wght@600;700;800&family=Poppins:wght@400;500;600;700;800&display=swap" rel="stylesheet">
<style>
:root{
  --orange:#e8501c;
  --black:#151515;
  --charcoal:#262626;
  --white:#ffffff;
  --light:#e9e9e9;
  --stage:#6a6a6a;
}
*{margin:0;padding:0;box-sizing:border-box}
html,body{width:1200px;height:2617px;overflow:hidden;background:var(--stage)}
.canvas{position:relative;width:1200px;height:2617px}
.hanger{position:absolute;top:580px;width:458px;height:1213px;transform:scale(1.2);transform-origin:0 0;overflow:hidden;font-family:'Poppins',sans-serif;box-shadow:0 6px 18px rgba(0,0,0,.45)}
.hanger-front{left:40px}
.hanger-back{left:610px}
.hanger svg.shapes{position:absolute;inset:0;width:458px;height:1213px}
.txt{position:absolute;left:0;width:100%;text-align:center}

/* front */
.headline{top:228px;font-family:'Oswald',sans-serif;font-weight:600;font-size:78px;line-height:1;color:var(--white);letter-spacing:-1px;transform:scaleY(1.05)}
.subhead{top:306px;font-family:'Orbitron',sans-serif;font-weight:700;font-size:33px;color:var(--orange);letter-spacing:.5px}
.dashes{top:354px;display:flex;justify-content:center;gap:3px}
.dashes span{width:7px;height:6px;background:var(--orange)}
.question{top:384px;font-size:21px;line-height:22px;font-weight:500;color:var(--white)}
.covered{top:434px;font-size:27px;font-weight:800;color:var(--orange)}
.brand{font-family:'Poppins',sans-serif;font-weight:800;font-size:58px;line-height:1;letter-spacing:2px}
.brand-front{top:876px;color:var(--black)}
.brand-line{position:absolute;left:96px;width:266px;text-align:center;font-size:12.5px;letter-spacing:.8px;border-top:1.5px solid currentColor;padding-top:2px}
.brand-line-front{top:940px;color:var(--black)}
.phone-pill{position:absolute;left:32px;width:388px;height:40px;background:var(--orange);border-radius:20px;color:var(--white);font-weight:700;font-size:36px;letter-spacing:3px;line-height:40px;padding-left:44px;text-align:center}
.phone-pill svg{position:absolute;left:6px;top:4px;width:32px;height:32px}
.phone-front{top:974px}
.icon-pin,.icon-mail{position:absolute;left:219px;width:20px;height:20px}
.address{top:1050px;font-size:21px;line-height:26px;color:var(--black)}
.email{top:1130px;font-size:21px;color:var(--black)}
.web{font-weight:700;font-size:26px;letter-spacing:2.5px}
.web b{color:var(--orange);font-weight:700}
.web-front{top:1160px;color:var(--black)}

/* badge */
.badge{position:absolute;width:140px;height:140px}
.badge-text{position:absolute;inset:0;display:flex;flex-direction:column;align-items:center;justify-content:center;transform:rotate(-14deg);line-height:.95}
.badge-text .small{font-family:'Poppins',sans-serif;font-weight:500;font-size:19px;color:var(--white)}
.badge-text .big{font-family:'Oswald',sans-serif;font-weight:600;font-size:27px;color:var(--orange)}

/* back */
.our{position:absolute;left:122px;top:492px;width:216px;height:56px;background:var(--light);font-family:'Orbitron',sans-serif;font-weight:800;font-size:48px;line-height:58px;text-align:center;color:var(--black)}
.services{position:absolute;left:77px;top:548px;width:306px;height:56px;background:var(--orange);font-family:'Orbitron',sans-serif;font-weight:700;font-size:39px;line-height:56px;text-align:center;color:var(--white);box-shadow:0 3px 6px rgba(0,0,0,.3)}
.service-grid{position:absolute;left:37px;width:383px;display:grid;grid-template-columns:repeat(3,1fr);gap:0 5px}
.row-1{top:628px}
.row-2{top:793px}
.service{display:flex;flex-direction:column}
.service-photo{height:92px}
.service-label{height:45px;display:flex;align-items:center;justify-content:center;text-align:center;font-weight:600;font-size:16px;line-height:15px;color:var(--white)}
.label-orange{background:var(--orange)}
.label-black{background:var(--black)}
.brand-back{top:980px;color:var(--white)}
.brand-line-back{top:1048px;color:var(--white)}
.phone-back{top:1088px}
.web-back{top:1146px;color:var(--white)}
</style>
</head>
<body>
<div class="canvas">

  <!-- FRONT -->
  <section class="hanger hanger-front">
    <svg class="shapes" viewBox="0 0 458 1213" aria-hidden="true">
      <defs>
        <linearGradient id="front-dark" x1="0" y1="0" x2="0" y2="1">
          <stop offset="0" stop-color="#2a2a2a"/><stop offset="1" stop-color="#111"/>
        </linearGradient>
        <linearGradient id="front-white" x1="0" y1="0" x2="0" y2="1">
          <stop offset="0" stop-color="#ffffff"/><stop offset=".55" stop-color="#f4f4f4"/><stop offset="1" stop-color="#c9c9c9"/>
        </linearGradient>
      </defs>
      <rect width="458" height="1213" fill="url(#front-dark)"/>
      <polygon points="0,670 458,470 458,700 0,700" fill="var(--orange)"/>
      <polygon points="0,905 230,772 458,905 458,1213 0,1213" fill="url(#front-white)"/>
      <rect x="0" y="122" width="170" height="15" fill="var(--stage)"/>
      <circle cx="230" cy="130" r="74" fill="var(--stage)"/>
    </svg>
    <svg class="shapes" viewBox="0 0 458 1213" role="img" aria-label="Photo of a remodelled grey-sided house with a covered porch in snow">
      <defs>
        <linearGradient id="house-photo" x1="0" y1="0" x2="1" y2="1">
          <stop offset="0" stop-color="#8a8f96"/><stop offset=".5" stop-color="#4b5058"/><stop offset="1" stop-color="#d8dadc"/>
        </linearGradient>
      </defs>
      <polygon points="0,665 458,430 458,690 230,765 0,690" fill="url(#house-photo)"/>
    </svg>

    <div class="txt headline">REMODELLING</div>
    <div class="txt subhead">&amp; RESTORATION</div>
    <div class="txt dashes"><span></span><span></span><span></span><span></span><span></span></div>
    <div class="txt question">THINKING YOU NEED A MORE<br>HOST-FRIENDLY SPACE?</div>
    <div class="txt covered">WE GOT YOU COVERED</div>

    <div class="badge" style="left:292px;top:750px">
      <svg viewBox="0 0 140 140" width="140" height="140" aria-hidden="true">
        <polygon fill="var(--black)" points="70,2 80,14 95,7 99,22 115,21 113,37 128,42 120,56 133,66 121,77 130,91 115,96 117,112 101,112 97,128 82,122 70,134 58,122 43,128 39,112 23,112 25,96 10,91 19,77 7,66 20,56 12,42 27,37 25,21 41,22 45,7 60,14"/>
      </svg>
      <div class="badge-text"><span class="small">WE ALSO</span><span class="small">OFFER</span><span class="big">FINANCING</span></div>
    </div>

    <div class="txt brand brand-front">HVR</div>
    <div class="brand-line brand-line-front">REMODELING &amp; RESTORATION</div>

    <div class="phone-pill phone-front">
      <svg viewBox="0 0 32 32" aria-hidden="true"><circle cx="16" cy="16" r="15" fill="var(--black)" stroke="var(--white)" stroke-width="2"/><path d="M11 8l3 4-2 2c1 2.5 3 4.5 5.5 5.5l2-2 4 3-1.5 3c-7 0-13-6-13-13z" fill="var(--white)"/></svg>
      555-010-2480
    </div>

    <svg class="icon-pin" style="top:1024px" viewBox="0 0 20 20" aria-hidden="true"><path d="M10 1a6 6 0 0 0-6 6c0 5 6 12 6 12s6-7 6-12a6 6 0 0 0-6-6z" fill="var(--orange)"/><circle cx="10" cy="7" r="2.3" fill="var(--white)"/></svg>
    <div class="txt address">218 NW Harbor Lane<br>Suite 12</div>
    <svg class="icon-mail" style="top:1108px" viewBox="0 0 20 20" aria-hidden="true"><rect x="2" y="5" width="16" height="11" fill="var(--orange)"/><path d="M2 5l8 6 8-6" fill="none" stroke="var(--white)" stroke-width="1.5"/></svg>
    <div class="txt email">hvrsolutions@mailbox.com</div>
    <div class="txt web web-front">www.<b>hvrremodel</b>.com</div>
  </section>

  <!-- BACK -->
  <section class="hanger hanger-back">
    <svg class="shapes" viewBox="0 0 458 1213" aria-hidden="true">
      <defs>
        <linearGradient id="back-white" x1="0" y1="0" x2="0" y2="1">
          <stop offset="0" stop-color="#ffffff"/><stop offset=".55" stop-color="#f2f2f2"/><stop offset=".8" stop-color="#cfcfcf"/>
        </linearGradient>
      </defs>
      <rect width="458" height="1213" fill="url(#back-white)"/>
      <polygon points="0,320 458,310 458,485 230,395 0,485" fill="var(--orange)"/>
      <polygon points="0,1060 230,945 458,1060 458,1213 0,1213" fill="var(--black)"/>
      <rect x="0" y="0" width="458" height="122" fill="#161616"/>
    </svg>
    <svg class="shapes" viewBox="0 0 458 1213" role="img" aria-label="Photo of a grey house with a new covered back porch and lawn">
      <defs>
        <linearGradient id="porch-photo" x1="0" y1="0" x2="0" y2="1">
          <stop offset="0" stop-color="#2e3136"/><stop offset=".45" stop-color="#6c747e"/><stop offset="1" stop-color="#5d6b45"/>
        </linearGradient>
      </defs>
      <polygon points="0,137 458,137 458,315 210,440 0,330" fill="url(#porch-photo)"/>
      <rect x="0" y="122" width="170" height="15" fill="var(--stage)"/>
      <circle cx="230" cy="130" r="74" fill="var(--stage)"/>
    </svg>

    <div class="badge" style="left:315px;top:378px">
      <svg viewBox="0 0 140 140" width="140" height="140" aria-hidden="true">
        <polygon fill="var(--black)" points="70,2 80,14 95,7 99,22 115,21 113,37 128,42 120,56 133,66 121,77 130,91 115,96 117,112 101,112 97,128 82,122 70,134 58,122 43,128 39,112 23,112 25,96 10,91 19,77 7,66 20,56 12,42 27,37 25,21 41,22 45,7 60,14"/>
      </svg>
      <div class="badge-text"><span class="small">WE ALSO</span><span class="small">OFFER</span><span class="big">FINANCING</span></div>
    </div>

    <div class="our">OUR</div>
    <div class="services">SERVICES</div>

    <div class="service-grid row-1">
      <div class="service"><div class="service-photo" role="img" aria-label="Photo of a finished basement floor" style="background:linear-gradient(#c9c3bd,#8a817a)"></div><div class="service-label label-orange">Basements</div></div>
      <div class="service"><div class="service-photo" role="img" aria-label="Photo of a house addition" style="background:linear-gradient(#b7c3d0,#6c7a66)"></div><div class="service-label label-black">Additions</div></div>
      <div class="service"><div class="service-photo" role="img" aria-label="Photo of a remodelled bathroom vanity" style="background:linear-gradient(#eee4d8,#a07a55)"></div><div class="service-label label-orange">Kitchens/<br>bathrooms</div></div>
    </div>
    <div class="service-grid row-2">
      <div class="service"><div class="service-photo" role="img" aria-label="Photo of damaged wood for mold and asbestos work" style="background:linear-gradient(#6e5a4d,#3e322b)"></div><div class="service-label label-orange">Mold/<br>Asbestos</div></div>
      <div class="service"><div class="service-photo" role="img" aria-label="Photo of a shingled roof" style="background:linear-gradient(#d5d6d6,#6f6a63)"></div><div class="service-label label-black">Roofing</div></div>
      <div class="service"><div class="service-photo" role="img" aria-label="Photo of a house with blue siding" style="background:linear-gradient(#dfe6ef,#47608a)"></div><div class="service-label label-orange">Siding</div></div>
    </div>

    <div class="txt brand brand-back">HVR</div>
    <div class="brand-line brand-line-back">REMODELING &amp; RESTORATION</div>

    <div class="phone-pill phone-back">
      <svg viewBox="0 0 32 32" aria-hidden="true"><circle cx="16" cy="16" r="15" fill="var(--black)" stroke="var(--white)" stroke-width="2"/><path d="M11 8l3 4-2 2c1 2.5 3 4.5 5.5 5.5l2-2 4 3-1.5 3c-7 0-13-6-13-13z" fill="var(--white)"/></svg>
      555-010-2480
    </div>
    <div class="txt web web-back">www.<b>hvrremodel</b>.com</div>
  </section>

</div>
</body>
</html>
```